Mobile Repair Service on location needs a Web Design

We are starting a new mobile device repair service called Gadget Haven and our website needs a design!

Hello Designers!
First, we'd like to make clear this is more than a simple web design contest, we want the designers to create an idea. We want someone who can create the whole theme of the service's we provide. We want someone that can help design our visual branding, help us communicate a sentiment. And we are willing to pay for that.

Who are we?
Our company is based in Rotterdam, the Netherlands. We provide different services for all kinds of electronic devices. The kind of services we provide are, among other things, installations of hardware and software and the repair of broken or malfunctioning devices.
We are starting a new service that offers mobile device repairs on location, be it at the home of our customers, their office, or any other place. Just give us the address and we will come to you for the repair job. This is also our main USP. We have multiple skilled engineers who drive trough the country on a daily basis and can be on location within a working day. Repair is done immediately onsite while the customer waits. At this stage we will start with the smartphone product-group within the mobile devices. In a second phase we might also add tablets.
People don't want to be without their phone for weeks because of some parts that needed to be ordered by a repair center they had to sent their phone to. We offer a fully functional mobile repair center in the form of specially customized vans. These vans have all the tools and utilities needed by our engineers to safely repair your mobile device. Your phone is being repaired directly in front of you, the next business-day, on a location you desire.

For this new service we are creating a website called Gadget Haven. The website needs a story and matching design and this is where you come in. We are not looking for a simple template design we can get from any place. We need a story. We want you to create an idea, build a unique theme or vision that helps sell the product/service. This goes beyond the design of the website. We need the whole package, the design you are creating needs to have returning elements like icons, color use, images, maybe even characters etc. You name it! There needs to be a common thread in the design so we can reuse elements in, for example, the email templates, the work order or receipt we give to our customers (we may contact the winner of the contest to design these for us as well!).

The name 'Gadget Haven' is chosen. Haven (short for rehabilitate) has a bold and playful tone to it and the design needs to reflect the name. So we're looking for a somewhat playful and cheeky design. Definitely not too serious and definitely modern. We already got a logo that we love and that fit's this description (see attached design documents for the logo). It's bold, powerful and fun. Our web design needs to reflect this as well and has to fit in with our logo.
We would really like it if the design somehow incorporates elements that highlight our unique selling points (repairs on location, we come to you etc.). We would really like some form of story telling in the design. Think clumsy people breaking their phones. Teenagers in tears because they have no access to their friends. People nowadays have the need to always be 'connected'. What happens when your phone is broken or malfunctioning? We're handling tech, we are nerds and a little bit weird, but we're professionals and here to help you with your problem. The sentiment Wire Troop tries to communicate is something we really like. We're looking for fresh idea's, anything goes!

In an overview all Unique Selling Points of the Gadget haven service:
- Professional service on location. Don’t ship to us we will come to you!
- Clear pricing upfront. No hidden cost.
- Next business-day repair.
- Backed by a professional call center open 12 hours a day and open on a Saturday as well
- Backed by a professional repair center with more then 12 years of experience
- Repair is done by certified engineers
- 1 year warranty on the repair

The process:
The main function of our website will be for customers to make a repair request. A customer will visit our website and can make a repair request immediately by going through a 'request-order-flow'. In this flow he or she will need to fill in some forms and can select wich type/model/brand of mobile device he or she has and what parts need to be repaired. After a request is placed we will call the customer back (within an hour) for a short intake and to set a date/time and location. Our engineer will meet the customer at the specified location and will repair the device onsite in one of our mobile repair centers, which is a specialized van equipped with all the tools needed for device restorations.
So in short the steps are:
- Choose your device and repair job
- Place the order
- Get a callback within the hour
- Set date and location
- We will come to you.

Website functionality:
Our website is our main form of communication. So the sentiment we want to communicate needs be reflected in the design. We need a main/front page designed (preferably a long scrolling page design) containing:
1. Customers will be able to request a repair job directly on our website. So there will need to be a prominent button/link at the top of our main page that will bring the customer to this 'request-order-flow'. This is the main flow which needs to be full focus on the front page. All other items are secondary.
2. The general information of who we are and what we do, and why the customer should choose us. Preferably in short bullet-point type keywords/sentences with icons or other visual cues. See our unique selling points to get an idea of the information that will be displayed here.
3. There needs to be a section that will explain the process (see above) of a repair request step-by- step, again in brief short key sentences and with (custom) icons.
4. There needs to be a section that explains to the customer he/she can always contact us if they are not sure what the problem is with their device, and for this reason are not sure what repair request they should order.
5. We want to implement some functionality that display customer ratings or customer reviews. So there needs to be room for some kind of widget of plugin we're going to implement which shows these reviews.
6. A 'For business section' where we will explain all the options we provide for corporate clients.
7. Social media links.
8. There needs to be a menu with buttons that leads to the all sections described in the previous points.

For now, we need a design for our front page. In the second phase, when we have picked our winner, we may ask the winner to design the page(s) for our request workflow as well.

EDIT:
Finally, we have a very specific order in mind for the different segments of our website. We would like you to add some more segments that were not in our original brief as well:

1. Top header with order/request button. (should instantly make clear our main USP, we do repairs on location)
2. Our process
3. Our unique selling points / why choose us
4. The kind of repairs we do (broken screens, broken batteries, water damage, broken camera's, no sound etc.)
5. A 'meet our team' section, where we introduce some of our engineers
6. A 'contact us for any questions' section/
7. Testimonials/user reviews
8. A section where we show key performance indicators
9. 'For businesses' sections
10.'Subscribe for newsletter' field
11. Social media buttons

Industry/Entity Type

It Service

Number of Pages Required

1 page

Font styles to use
Sans Serif

Requirements
Must have
• a main/front page, design only
• custom icons/images for banners, adverts online and in print (high res)
Nice to have
• Storytelling in our design.
• Design that fits with our brand new logo.
• Elements like icons to have a flat design.
• Keep in mind that the website will need to be responsive when designing! (Ideally provide an example of the mobile design as well)
• Create a fun and trustworthy feeling.

```html
<!DOCTYPE html>
<html lang="en">
<head>
<meta charset="utf-8">
<title>Gadget Haven – Mobile repair on location</title>
<link rel="stylesheet" href="https://fonts.googleapis.com/css2?family=Montserrat:wght@300;400;500;700&family=Lora:ital@1&display=swap">
<style>
  :root {
    --cream: #fdf6dc;
    --orange: #ff8a00;
    --orange-soft: #ffd59a;
    --ink: #222222;
    --ink-soft: #555555;
    --ice: #e3f4f8;
    --night: #161616;
    --footer: #1c1c1c;
    --green: #2db34a;
    --blue: #2e8fe6;
    --band: #1e8df5;
    --white: #ffffff;
    --rule: #e2e2e2;
    --review-green: #3d9a6a;
  }
  * { box-sizing: border-box; margin: 0; padding: 0; }
  html, body { width: 1200px; height: 2908px; overflow: hidden; }
  body { font-family: "Montserrat", Arial, sans-serif; color: var(--ink); background: var(--white); position: relative; }
  section, header, footer { position: absolute; left: 0; width: 1200px; }
  .abs { position: absolute; }

  /* Hero */
  .hero { top: 0; height: 675px; background: var(--cream); }
  .brand { left: 128px; top: 34px; display: flex; align-items: center; gap: 14px; }
  .brand-dot { width: 52px; height: 52px; border-radius: 50%; background: var(--orange); }
  .brand-name { font-weight: 700; font-size: 26px; line-height: 1; color: var(--ink); letter-spacing: .5px; }
  .main-nav { right: 128px; top: 56px; display: flex; gap: 38px; font-size: 12.5px; font-weight: 500; letter-spacing: .3px; }
  .main-nav a { color: var(--ink); text-decoration: none; }
  .hero-title { left: 124px; top: 182px; font-size: 29px; font-weight: 700; letter-spacing: .3px; }
  .hero-sub { left: 147px; top: 221px; font-size: 21px; font-weight: 300; }
  .doorstep-badge { left: 254px; top: 258px; width: 182px; height: 182px; border-radius: 50%; background: var(--orange-soft); }
  .doorstep-badge .inner { position: absolute; left: 19px; top: 19px; width: 144px; height: 144px; border-radius: 50%; background: var(--orange); }
  .doorstep-title { left: 200px; top: 458px; width: 290px; text-align: center; font-size: 23px; font-weight: 300; line-height: 29px; }
  .doorstep-sub { left: 160px; top: 524px; width: 370px; text-align: center; font-size: 17.5px; font-weight: 300; }
  .btn { display: flex; align-items: center; justify-content: center; font-weight: 700; font-size: 17px; letter-spacing: .4px; text-decoration: none; }
  .btn-orange { left: 223px; top: 574px; width: 244px; height: 62px; background: var(--orange); color: var(--white); }
  .hero-art { left: 624px; top: 178px; width: 442px; height: 462px; border-radius: 24px; background: linear-gradient(160deg, #bfece6 0%, #f6d8cf 60%, #f3e3b6 100%); }

  /* Why */
  .why { top: 675px; height: 675px; background: var(--ice); }
  .section-title { width: 1200px; text-align: center; font-size: 32px; font-weight: 300; }
  .why .section-title { top: 36px; }
  .why .section-title strong { color: var(--orange); font-weight: 700; }
  .usp { display: flex; gap: 28px; width: 420px; }
  .usp svg { flex: none; width: 70px; height: 70px; }
  .usp h3 { font-size: 18.5px; font-weight: 700; line-height: 23px; letter-spacing: .3px; text-transform: uppercase; }
  .usp p { font-size: 18.5px; font-weight: 400; line-height: 23px; color: var(--ink-soft); margin-top: 3px; }

  /* Process */
  .process { top: 1350px; height: 674px; background: var(--night); color: var(--white); }
  .process .section-title { top: 112px; line-height: 38px; }
  .process .section-title strong { color: var(--green); font-weight: 700; display: block; }
  .step-icon { width: 80px; height: 80px; }
  .timeline { left: 205px; top: 424px; width: 810px; height: 28px; }
  .step-text { width: 220px; text-align: center; color: var(--blue); font-size: 18.5px; line-height: 22px; }
  .step-text h4 { font-weight: 700; text-transform: uppercase; }
  .step-text p { font-weight: 400; }

  /* CTA band */
  .cta-band { top: 2024px; height: 159px; background: var(--band); color: var(--white); }
  .cta-band h2 { left: 124px; top: 46px; font-size: 18.5px; font-weight: 700; }
  .cta-band p { left: 124px; top: 72px; width: 420px; font-size: 18.5px; line-height: 22px; }
  .btn-white { left: 830px; top: 49px; width: 244px; height: 62px; background: var(--white); color: var(--band); }

  /* Reviews */
  .reviews { top: 2183px; height: 522px; background: var(--white); }
  .reviews-kicker { top: 70px; width: 1200px; text-align: center; font-family: "Lora", Georgia, serif; font-style: italic; font-size: 18px; }
  .reviews-title { top: 96px; width: 1200px; text-align: center; font-size: 31px; font-weight: 500; }
  .rule { height: 1px; background: var(--rule); }
  .score-card { left: 74px; top: 167px; width: 236px; height: 177px; border: 1px solid var(--rule); text-align: center; }
  .score-card h3 { margin-top: 18px; font-size: 21px; font-weight: 500; }
  .stars { color: var(--review-green); font-size: 15px; letter-spacing: 3px; }
  .score-card .stars { margin-top: 8px; font-size: 17px; }
  .score-card .count { font-family: "Lora", Georgia, serif; font-style: italic; font-size: 13px; margin-top: 8px; }
  .score-card .see-all { position: absolute; left: 48px; top: 126px; display: flex; align-items: center; gap: 10px; font-size: 12px; font-weight: 700; color: var(--review-green); }
  .circle-btn { width: 36px; height: 36px; border-radius: 50%; border: 1.5px solid var(--rule); display: flex; align-items: center; justify-content: center; color: var(--ink); font-size: 14px; }
  .review { width: 210px; top: 168px; }
  .review h4 { font-size: 21px; font-weight: 500; line-height: 26px; margin-top: 10px; }
  .review blockquote { font-family: "Lora", Georgia, serif; font-style: italic; font-size: 14px; line-height: 19px; color: var(--ink-soft); margin-top: 6px; height: 76px; }
  .review .who { font-size: 11.5px; font-weight: 700; color: var(--review-green); margin-top: 8px; }
  .review .when { font-size: 10px; color: #999; }
  .pager { left: 554px; top: 403px; display: flex; gap: 10px; }
  .pager .circle-btn { width: 40px; height: 40px; border: 2px solid var(--review-green); color: var(--review-green); font-weight: 700; }

  /* Footer */
  .site-footer { top: 2705px; height: 203px; background: var(--footer); color: var(--white); }
  .contact { left: 124px; top: 28px; font-size: 18.5px; line-height: 35px; }
  .contact h2 { font-size: 18.5px; font-weight: 700; }
  .follow { left: 727px; top: 28px; font-size: 18.5px; line-height: 35px; }
  .socials { left: 733px; top: 88px; display: flex; gap: 70px; }
  .socials span { width: 30px; height: 30px; border-radius: 50%; background: var(--white); display: block; }
</style>
</head>
<body>

<header class="hero">
  <div class="brand abs">
    <span class="brand-dot"></span>
    <span class="brand-name">GADGET<br>HAVEN</span>
  </div>
  <nav class="main-nav abs">
    <a href="#why">WHY GADGET HAVEN</a>
    <a href="#how">HOW IT WORKS</a>
    <a href="#reviews">CUSTOMER REVIEWS</a>
    <a href="#contact">CONTACT</a>
  </nav>
  <h1 class="hero-title abs">BROKEN PHONE OR TABLET?</h1>
  <p class="hero-sub abs">We are the solution to your problems</p>
  <div class="doorstep-badge abs">
    <div class="inner">
      <svg width="144" height="144" viewBox="0 0 144 144" aria-hidden="true">
        <rect x="52" y="36" width="40" height="72" fill="#fff"/>
        <polygon points="62,40 86,34 86,110 62,104" fill="#ffe2b8"/>
        <circle cx="80" cy="73" r="3" fill="#ff8a00"/>
      </svg>
    </div>
  </div>
  <p class="doorstep-title abs">WE COME TO YOUR DOORSTEP</p>
  <p class="doorstep-sub abs">The quickest way to repair your device</p>
  <a class="btn btn-orange abs" href="#request">REQUEST A REPAIR</a>
  <div class="hero-art abs" role="img" aria-label="Illustration of a smiling bandaged phone connected to a multimeter, with a screwdriver beside it"></div>
</header>

<section class="why" id="why">
  <h2 class="section-title abs">WHY <strong>GADGET HAVEN?</strong></h2>

  <div class="usp abs" style="left:155px;top:163px;">
    <svg viewBox="0 0 70 70" aria-hidden="true"><path d="M4 30 L20 20 L34 30 L48 20 L66 30 L58 44 L44 52 L30 50 L14 44 Z" fill="#2e6fd6"/><path d="M20 36 L34 30 L46 40 L36 48 Z" fill="#1a4da3"/></svg>
    <div><h3>Professional service<br>on location.</h3><p>Don't ship to us we will<br>come to you!</p></div>
  </div>
  <div class="usp abs" style="left:155px;top:330px;">
    <svg viewBox="0 0 70 70" aria-hidden="true"><circle cx="35" cy="35" r="33" fill="#2e8fe6"/><text x="35" y="48" text-anchor="middle" font-family="Montserrat, sans-serif" font-weight="700" font-size="38" fill="#fff">$</text></svg>
    <div><h3>Clear pricing<br>upfront.</h3><p>No hidden cost.</p></div>
  </div>
  <div class="usp abs" style="left:155px;top:495px;">
    <svg viewBox="0 0 70 70" aria-hidden="true"><rect x="6" y="24" width="38" height="28" fill="#2e8fe6"/><path d="M44 32 H58 L66 42 V52 H44 Z" fill="#1a6fc4"/><circle cx="18" cy="56" r="7" fill="#222"/><circle cx="54" cy="56" r="7" fill="#222"/><circle cx="12" cy="14" r="10" fill="#fff" stroke="#222" stroke-width="3"/><path d="M12 8 V14 H17" stroke="#222" stroke-width="2.5" fill="none"/></svg>
    <div><h3>Next business-day<br>repair.</h3></div>
  </div>

  <div class="usp abs" style="left:651px;top:163px;width:430px;">
    <svg viewBox="0 0 70 70" aria-hidden="true"><path d="M18 30 A17 17 0 0 1 52 30" stroke="#2e8fe6" stroke-width="5" fill="none"/><rect x="12" y="28" width="9" height="14" rx="3" fill="#2e8fe6"/><rect x="49" y="28" width="9" height="14" rx="3" fill="#2e8fe6"/><path d="M8 68 Q8 48 35 48 Q62 48 62 68 Z" fill="#2e8fe6"/></svg>
    <div><h3>12 hour call center</h3><p>Backed by a professional call<br>center open 12 hours a day and<br>open on a Saturday as well</p></div>
  </div>
  <div class="usp abs" style="left:651px;top:330px;width:430px;">
    <svg viewBox="0 0 70 70" aria-hidden="true"><path d="M24 40 L18 66 L28 60 L34 68 L38 44 Z M46 40 L52 66 L42 60 L36 68 L32 44 Z" fill="#1a6fc4"/><circle cx="35" cy="28" r="22" fill="#2e8fe6"/><circle cx="35" cy="28" r="13" fill="#fff"/><circle cx="35" cy="28" r="7" fill="#2e8fe6"/></svg>
    <div><h3>Repair is done by certified<br>engineers</h3><p>Backed by a professional repair<br>center with more then 12 years of<br>experience.</p></div>
  </div>
  <div class="usp abs" style="left:651px;top:495px;width:430px;">
    <svg viewBox="0 0 70 70" aria-hidden="true"><rect x="16" y="4" width="38" height="62" rx="3" fill="#2e8fe6"/><rect x="21" y="12" width="28" height="44" fill="#bfe0ff"/><path d="M27 44 V34 H31 L36 24 Q40 24 39 30 L38 33 H44 V44 Z" fill="#1a4da3"/></svg>
    <div><h3>1 year warranty on the<br>repair.</h3><p>We offer lightening fast<br>turnarounds. No hassle,<br>Guaranteed!</p></div>
  </div>
</section>

<section class="process" id="how">
  <h2 class="section-title abs">HOW IT WORKS.<strong>WE COME TO YOU</strong></h2>

  <svg class="step-icon abs" style="left:183px;top:312px;" viewBox="0 0 80 80" aria-hidden="true"><rect x="26" y="12" width="28" height="50" rx="3" fill="none" stroke="#2e8fe6" stroke-width="3"/><path d="M34 42 L46 28" stroke="#fff" stroke-width="2"/><circle cx="40" cy="56" r="2" fill="#2e8fe6"/></svg>
  <svg class="step-icon abs" style="left:445px;top:312px;" viewBox="0 0 80 80" aria-hidden="true"><rect x="14" y="32" width="34" height="22" fill="#2e8fe6"/><path d="M48 38 H60 L68 48 V54 H48 Z" fill="#1a6fc4"/><circle cx="24" cy="58" r="6" fill="#fff"/><circle cx="58" cy="58" r="6" fill="#fff"/><circle cx="20" cy="18" r="10" fill="none" stroke="#2db34a" stroke-width="3"/><path d="M15 18 L19 22 L26 14" stroke="#2db34a" stroke-width="3" fill="none"/></svg>
  <svg class="step-icon abs" style="left:703px;top:312px;" viewBox="0 0 80 80" aria-hidden="true"><rect x="10" y="16" width="48" height="44" rx="3" fill="none" stroke="#2e8fe6" stroke-width="3"/><path d="M10 26 H58" stroke="#2e8fe6" stroke-width="3"/><path d="M20 10 V20 M30 10 V20 M40 10 V20 M50 10 V20" stroke="#2e8fe6" stroke-width="3"/><text x="34" y="52" text-anchor="middle" font-family="Montserrat, sans-serif" font-weight="700" font-size="20" fill="#2e8fe6">23</text><circle cx="60" cy="58" r="12" fill="#161616" stroke="#2db34a" stroke-width="3"/><path d="M54 58 L58 62 L66 54" stroke="#2db34a" stroke-width="3" fill="none"/></svg>
  <svg class="step-icon abs" style="left:962px;top:312px;" viewBox="0 0 80 80" aria-hidden="true"><rect x="26" y="20" width="28" height="46" rx="3" fill="none" stroke="#2e8fe6" stroke-width="3"/><path d="M33 44 L38 49 L47 38" stroke="#2db34a" stroke-width="3" fill="none"/><path d="M62 6 V16 M57 11 H67 M14 36 V44 M10 40 H18" stroke="#2db34a" stroke-width="2"/></svg>

  <svg class="timeline abs" viewBox="0 0 810 28" aria-hidden="true">
    <g fill="none" stroke="#2e8fe6" stroke-width="3"><circle cx="18" cy="14" r="9"/><circle cx="280" cy="14" r="9"/><circle cx="538" cy="14" r="9"/><circle cx="797" cy="14" r="9"/></g>
    <g stroke="#2e8fe6" stroke-width="1.5"><path d="M36 14 H258"/><path d="M298 14 H516"/><path d="M556 14 H775"/></g>
    <g fill="#2e8fe6"><path d="M258 10 L266 14 L258 18 Z"/><path d="M516 10 L524 14 L516 18 Z"/><path d="M775 10 L783 14 L775 18 Z"/></g>
  </svg>

  <div class="step-text abs" style="left:113px;top:484px;"><h4>Tell us the<br>problem.</h4><p>Choose your device<br>and repair job.</p></div>
  <div class="step-text abs" style="left:375px;top:484px;"><h4>Place the order.</h4><p>Get a callback within<br>the hour.</p></div>
  <div class="step-text abs" style="left:633px;top:484px;"><h4>Set date and<br>location</h4><p>We recieve your<br>order and confirm<br>appointment.</p></div>
  <div class="step-text abs" style="left:892px;top:484px;"><h4>We fix your<br>device</h4><p>We will come to<br>you and fix your<br>device.</p></div>
</section>

<section class="cta-band" id="request">
  <h2 class="abs">DO YOU NEED A MOBILE PHONE REPAIR?</h2>
  <p class="abs">Choose your device and repair job. We will come to you.</p>
  <a class="btn btn-white abs" href="#request">REQUEST A REPAIR</a>
</section>

<section class="reviews" id="reviews">
  <div class="rule abs" style="left:0;top:101px;width:490px;"></div>
  <div class="rule abs" style="left:710px;top:101px;width:490px;"></div>
  <p class="reviews-kicker abs">What our customers</p>
  <h2 class="reviews-title abs">Are Saying</h2>

  <div class="score-card abs">
    <h3>Excellent</h3>
    <div class="stars">★★★★★</div>
    <p class="count">Based on 1,979 reviews</p>
    <div class="see-all">See all reviews <span class="circle-btn">›</span></div>
  </div>

  <article class="review abs" style="left:361px;">
    <div class="stars">★★★★☆</div>
    <h4>As good as advertised</h4>
    <blockquote>"Great service at the right price"</blockquote>
    <p class="who">Mrs Anna Verhoef</p><p class="when">44 Hours Ago</p>
  </article>
  <article class="review abs" style="left:609px;">
    <div class="stars">★★★☆☆</div>
    <h4>Excellent service and good quality</h4>
    <blockquote>"Placed my order. Arrived on time, fixed me up and I was good again."</blockquote>
    <p class="who">Mrs Julia Brandt</p><p class="when">About 1 hour ago</p>
  </article>
  <article class="review abs" style="left:859px;">
    <div class="stars">★★★★☆</div>
    <h4>Efficient and helful in every way</h4>
    <blockquote>"Cried when my phone broke... but you guys saved me. Y'all were helpful and efficient"</blockquote>
    <p class="who">Mr Tom Hollis</p><p class="when">4 days ago</p>
  </article>

  <div class="rule abs" style="left:0;top:421px;width:1200px;"></div>
  <div class="pager abs"><span class="circle-btn">‹</span><span class="circle-btn">›</span></div>
</section>

<footer class="site-footer" id="contact">
  <div class="contact abs">
    <h2>CONTACT US</h2>
    <p>1-800-555-0142</p>
    <p>45 Harbour lane, Rotterdam</p>
    <p>hello@gadgethaven.example</p>
  </div>
  <p class="follow abs">Follow Us</p>
  <div class="socials abs" aria-label="Social media links"><span></span><span></span><span></span><span></span></div>
</footer>

</body>
</html>
```